Company Values Graphic

We are looking for a design of our company values that can be used in a variety of places including our website, mousepads, office posters, business cards, etc.

Notes:
- We'd rather have icons/art than photographs on the poster.... so more like an infographic
- The core value group headings are not required, but can be included if you think grouping the values works for your design
- We have a logo for our software product but that logo is not required
- We don't need/want clever images to accompany each value, but some images are fine
- BrisKel logo attached
- BrisKel colors are attached
- BrisKel logo is Nunito Sans ExtraBold 800
- BrisKel website uses Roboto

Our Values - Who we will work with (and who we will not)
The right set of values are essential to building and maintaining a culture that we all wake up eager to be a part of each day. They are foundational to all hiring and firing decisions. They attract the right people and repel the wrong ones.

BE HELPFUL
Make every person and place better because you are there.
Deliver wow with every interaction.

BE HUMBLE
Listen with every muscle.
Passionately help others first.
Seek first to understand.

BE HONEST
Earn trust every day.
Be open and direct.
Treat everyone with fairness and respect.

BE HUMAN
Celebrate passion and action.
Create an environment where people are authentic.
Hire great people and expect a lot from them

BE COURAGEOUS
Dare mighty things.
Make and honor commitments.
All great things start with a small act of courage applied at the right moment.

```html
<!DOCTYPE html>
<html lang="en">
<head>
<meta charset="utf-8">
<title>BrisKel — Our Values</title>
<link rel="stylesheet" href="https://fonts.googleapis.com/css2?family=Montserrat:wght@400;500;600;700;800;900&display=swap">
<style>
  :root {
    --red: #ed2427;
    --orange: #f05a28;
    --amber: #f7941d;
    --paper: #f1f1f3;
    --white: #ffffff;
    --ink: #111111;
    --grey-text: #8a8a8f;
  }
  * { box-sizing: border-box; margin: 0; padding: 0; }
  html, body { width: 667px; height: 1200px; overflow: hidden; }
  body {
    background: var(--paper);
    font-family: "Montserrat", Arial, sans-serif;
    color: var(--ink);
  }
  .values-board {
    width: 667px;
    height: 1200px;
    display: grid;
    grid-template-columns: 333.5px 333.5px;
    grid-template-rows: repeat(6, 200px);
  }
  .tile { position: relative; overflow: hidden; }
  .tile--red { background: var(--red); }
  .tile--orange { background: var(--orange); }
  .tile--amber { background: var(--amber); }
  .tile--paper { background: var(--paper); }

  .intro {
    grid-column: span 2;
    background: var(--white);
    padding: 16px 40px 0;
    text-align: center;
  }
  .brand {
    display: flex;
    align-items: center;
    justify-content: center;
    gap: 22px;
    height: 62px;
  }
  .brand__dot {
    width: 58px; height: 58px;
    border-radius: 50%;
    background: var(--orange);
  }
  .brand__name {
    font-weight: 800;
    font-size: 54px;
    line-height: 1;
    letter-spacing: -1px;
    color: var(--ink);
  }
  .intro__title {
    font-weight: 900;
    font-size: 30px;
    line-height: 1.05;
    color: var(--red);
    letter-spacing: 0.5px;
    text-align: right;
    margin: 4px 60px 0 0;
  }
  .intro__subtitle {
    font-weight: 700;
    font-size: 13.5px;
    color: var(--grey-text);
    letter-spacing: 0.3px;
    margin-top: 6px;
  }
  .intro__text {
    font-size: 11.4px;
    line-height: 1.2;
    margin-top: 5px;
  }

  .value {
    padding: 0 22px 0 26px;
    display: flex;
    flex-direction: column;
    justify-content: center;
  }
  .value__title {
    font-weight: 900;
    font-size: 36px;
    line-height: 0.98;
    text-transform: uppercase;
    letter-spacing: 0.5px;
  }
  .value__title--long { font-size: 28px; }
  .value__text {
    font-size: 12.6px;
    line-height: 1.22;
    margin-top: 12px;
  }

  .icon-art {
    position: absolute;
    left: 50%; top: 50%;
    transform: translate(-50%, -50%);
    border: 9px solid var(--paper);
  }
  .icon-art--heart {
    width: 176px; height: 150px;
    border-radius: 50% 50% 46% 46% / 40% 40% 60% 60%;
    background: linear-gradient(135deg, var(--orange) 0%, var(--orange) 45%, var(--amber) 100%);
  }
  .icon-art--heart-person {
    width: 138px; height: 170px;
    border-radius: 50% 50% 18px 18px;
    background: linear-gradient(225deg, var(--amber) 0%, var(--orange) 40%, var(--red) 100%);
  }
  .icon-art--palm {
    width: 124px; height: 172px;
    border-radius: 40px 40px 62px 62px;
    background: linear-gradient(200deg, var(--amber) 0%, var(--orange) 55%, var(--red) 100%);
  }
  .icon-art--person {
    width: 148px; height: 172px;
    border-radius: 50% 50% 20px 20px / 38% 38% 20px 20px;
    background: linear-gradient(135deg, var(--red) 0%, var(--orange) 45%, var(--amber) 100%);
  }
  .icon-art--fist {
    width: 146px; height: 164px;
    border-radius: 36px 36px 14px 14px;
    background: linear-gradient(45deg, var(--red) 0%, var(--orange) 50%, var(--amber) 100%);
  }
</style>
</head>
<body>
  <main class="values-board">
    <header class="intro">
      <div class="brand">
        <span class="brand__dot"></span>
        <span class="brand__name">BrisKel</span>
      </div>
      <h1 class="intro__title">OUR VALUES</h1>
      <h2 class="intro__subtitle">WHO WE WILL WORK WITH (AND WHO WE WILL NOT)</h2>
      <p class="intro__text">The right set of values are essential to building and maintaining a culture that we all wake up eager to be a part of each day. They are foundational to all hiring and firing decisions. They attract the right people and repel the wrong ones.</p>
    </header>

    <div class="tile tile--red"><div class="icon-art icon-art--heart" role="img" aria-label="Icon of a heart formed by a handshake"></div></div>
    <section class="tile tile--paper value">
      <h3 class="value__title">Be<br>Helpful</h3>
      <p class="value__text">Make every person and place better because you are there. Deliver wow with every interaction.</p>
    </section>

    <section class="tile tile--paper value">
      <h3 class="value__title">Be<br>Humble</h3>
      <p class="value__text">Listen with every muscle. Passionately help others first. Seek first to understand.</p>
    </section>
    <div class="tile tile--orange"><div class="icon-art icon-art--heart-person" role="img" aria-label="Icon of a person with hand on heart"></div></div>

    <section class="tile tile--paper value">
      <h3 class="value__title">Be<br>Honest</h3>
      <p class="value__text">Earn trust every day. Be open and direct. Treat everyone with fairness and respect.</p>
    </section>
    <div class="tile tile--amber"><div class="icon-art icon-art--palm" role="img" aria-label="Icon of an open palm with a heart"></div></div>

    <div class="tile tile--red"><div class="icon-art icon-art--person" role="img" aria-label="Icon of a person silhouette"></div></div>
    <section class="tile tile--paper value">
      <h3 class="value__title">Be<br>Human</h3>
      <p class="value__text">Celebrate passion and action. Create an environment where people are authentic. Hire great people and expect a lot from them.</p>
    </section>

    <div class="tile tile--orange"><div class="icon-art icon-art--fist" role="img" aria-label="Icon of a raised fist"></div></div>
    <section class="tile tile--paper value">
      <h3 class="value__title value__title--long">Be<br>Courageous</h3>
      <p class="value__text">Dare mighty things. Make and honor commitments. All great things start with a small act of courage applied at the right moment.</p>
    </section>
  </main>
</body>
</html>
```